Danke für den tollen Flyer und die nette Zusammenarbeit. Gerne wieder.
Zielgruppe
Ich betreibe eine mobile Hundeschule / Hundetraining. Meine Zielgruppe sind Hundehalter:innen, junge Menschen und jung Gebliebene.
Aufgabenstellung
Das Design soll in erster Linie modern sein, aber auch kompetent und sympathisch wirken. Texte würde ich gerne in Absprache mit dem Designer erstellen.
Ich wünsche mir einen Faltflyer in Standardgröße (ich glaube das heißt DIN lang, 2 mal gefaltet (Wickelfalz), 99x210mm.
IM AMHANG SIND BILDER DER NEUEN HOMEPAGE. DIESE IST NCOH NICHT ONLINE. DAS DESIGN SOLL SICH GERNE AN DEN BILDERN DER HOMEPAGE ORIENTIEREN.

```html
<!DOCTYPE html>
<html lang="de">
<head>
<meta charset="utf-8">
<title>Hundeakademie Auental – Faltflyer</title>
<link rel="stylesheet" href="https://fonts.googleapis.com/css2?family=Arvo:wght@700&family=Fira+Sans:ital,wght@0,300;0,400;0,600;0,700;1,300&display=swap">
<style>
  :root {
    --gold: #e2b21f;
    --gold-soft: #f1d98a;
    --brown: #7b5434;
    --brown-dark: #5a3b23;
    --ink: #262120;
    --body: #8a6f5c;
    --panel: #ffffff;
    --panel-warm: #f1eeea;
    --page: #ffffff;
    --shadow: rgba(60, 40, 20, 0.14);
  }
  * { box-sizing: border-box; margin: 0; padding: 0; }
  html, body { width: 1200px; height: 2400px; overflow: hidden; background: var(--page); }
  body { position: relative; font-family: "Fira Sans", Arial, sans-serif; color: var(--ink); }

  .panel {
    position: absolute; width: 370px; height: 784px; background: var(--panel);
    box-shadow: 0 10px 30px var(--shadow); overflow: hidden;
  }
  .panel--warm { background: var(--panel-warm); }
  .panel::after {
    content: ""; position: absolute; left: 0; right: 0; bottom: 0; height: 8px; background: var(--brown);
  }

  .brand { display: flex; align-items: center; gap: 10px; }
  .brand__dot { width: 30px; height: 30px; border-radius: 50%; background: var(--gold); flex: none; }
  .brand__name { font-family: "Fira Sans", Arial, sans-serif; font-weight: 700; font-size: 20px; color: var(--brown); letter-spacing: 0.5px; text-transform: uppercase; line-height: 1.1; }

  .kicker { font-weight: 300; font-style: italic; color: var(--gold); font-size: 20px; }
  .kicker--small { font-size: 11px; font-style: normal; font-weight: 600; }
  .headline { font-family: "Arvo", Georgia, serif; font-weight: 700; color: var(--ink); line-height: 1.12; }

  .lead { font-weight: 700; color: var(--brown); font-size: 13px; line-height: 1.5; }
  .copy { font-weight: 300; color: var(--body); font-size: 13px; line-height: 1.55; letter-spacing: 0.4px; }

  .photo { position: absolute; }

  /* Cover */
  .cover { left: 215px; top: 80px; }
  .cover .brand { position: absolute; left: 32px; top: 40px; }
  .cover .kicker { position: absolute; left: 32px; top: 150px; }
  .cover .headline { position: absolute; left: 32px; top: 182px; font-size: 34px; }
  .cover .photo {
    left: 0; right: 0; top: 300px; bottom: 0;
    background: linear-gradient(180deg, #ffffff 0%, #d9d3cc 18%, #c89a66 50%, #a8612e 75%, #8b5a35 100%);
  }
  .offer-tags { position: absolute; left: 24px; bottom: 78px; display: flex; flex-direction: column; gap: 4px; }
  .offer-tag {
    align-self: flex-start; background: rgba(123, 84, 52, 0.85); color: var(--gold-soft);
    font-weight: 300; font-style: italic; font-size: 23px; padding: 1px 10px; line-height: 1.15;
  }
  .cover .url { position: absolute; left: 28px; bottom: 34px; color: #fff; font-weight: 700; font-size: 14px; }

  /* Photo & list panel */
  .services { left: 615px; top: 80px; }
  .services .photo {
    left: 30px; right: 30px; top: 30px; height: 250px; border-radius: 4px 4px 22px 4px;
    background: linear-gradient(180deg, #5a5a3a 0%, #8c7a48 45%, #a8843e 100%);
  }
  .check-list { position: absolute; left: 36px; top: 310px; list-style: none; }
  .check-list li { display: flex; align-items: center; gap: 14px; font-weight: 700; color: var(--brown-dark); font-size: 16px; margin-bottom: 14px; }
  .check-list .bullet { width: 22px; height: 22px; }
  .services .copy { position: absolute; left: 36px; right: 30px; }
  .services .copy--one { top: 440px; }
  .services .copy--two { top: 560px; }

  /* Intro panel */
  .intro { left: 20px; top: 964px; }
  .intro .brand { position: absolute; left: 36px; top: 40px; }
  .intro .kicker { position: absolute; left: 36px; top: 120px; }
  .intro .headline { position: absolute; left: 36px; top: 140px; font-size: 26px; }
  .intro .lead { position: absolute; left: 36px; right: 30px; top: 260px; }
  .intro .copy { position: absolute; left: 36px; right: 30px; top: 370px; }
  .intro .photo { left: 0; right: 0; bottom: 8px; height: 250px; background: linear-gradient(180deg, #ffffff 0%, #f1ece8 40%, #d9c3b3 100%); }

  /* Offers panel */
  .offers { left: 415px; top: 964px; }
  .offer { position: absolute; left: 40px; right: 24px; }
  .offer__img { width: 120px; height: 120px; border-radius: 50%; }
  .offer__label {
    position: absolute; left: 70px; top: 94px; background: rgba(123, 84, 52, 0.9); color: var(--gold-soft);
    font-weight: 300; font-size: 19px; padding: 0 10px; line-height: 1.3;
  }
  .offer__text { margin: 18px 0 0 92px; font-size: 11px; line-height: 1.45; }
  .offer__title { font-weight: 700; color: var(--brown-dark); font-size: 12px; }
  .offer__desc { color: var(--body); }
  .offer__target { color: var(--gold); font-weight: 300; }

  /* Right panel */
  .story { left: 810px; top: 964px; }
  .story .kicker { position: absolute; left: 32px; top: 44px; }
  .story .lead { position: absolute; left: 32px; right: 30px; font-size: 12px; font-style: italic; }
  .story .lead--one { top: 76px; }
  .story .lead--two { top: 160px; }
  .story .lead--three { top: 244px; }
  .story .badge { position: absolute; right: -30px; top: 360px; width: 90px; height: 90px; border-radius: 50%; background: var(--gold); }
  .story .photo { left: 0; right: 0; bottom: 8px; height: 360px; background: linear-gradient(180deg, #ffffff 0%, #b9c98a 22%, #7f9a4c 60%, #5f7a36 100%); }
</style>
</head>
<body>

  <!-- Cover -->
  <section class="panel cover">
    <div class="brand">
      <span class="brand__dot"></span>
      <span class="brand__name">Hundeakademie<br>Auental</span>
    </div>
    <p class="kicker">Hundeakademie Auental</p>
    <h1 class="headline">Entspannter und glücklicher Alltag mit Hund</h1>
    <div class="photo" role="img" aria-label="Foto eines lachenden rotbraunen Hundes auf einer Wiese"></div>
    <div class="offer-tags">
      <span class="offer-tag">Einzeltraining</span>
      <span class="offer-tag">Gruppentraining</span>
      <span class="offer-tag">Verhaltensberatung</span>
    </div>
    <p class="url">www.hundeakademie-auental.de</p>
  </section>

  <!-- Photo & list panel -->
  <section class="panel panel--warm services">
    <div class="photo" role="img" aria-label="Foto einer Trainerin, die auf einer Wiese kniet, während ein Hund auf sie zuläuft"></div>
    <ul class="check-list">
      <li><svg class="bullet" viewBox="0 0 22 22"><circle cx="11" cy="11" r="11" fill="var(--gold)"/></svg>Einzeltraining</li>
      <li><svg class="bullet" viewBox="0 0 22 22"><circle cx="11" cy="11" r="11" fill="var(--gold)"/></svg>Gruppentraining</li>
      <li><svg class="bullet" viewBox="0 0 22 22"><circle cx="11" cy="11" r="11" fill="var(--gold)"/></svg>Verhaltensberatung</li>
    </ul>
    <p class="copy copy--one">Dunt iliquid qui culless imusda porepel inveni­mus sin net et volor alit volesedit am qui am endaeperum im rentur? Ulloreptam aut el ipsunde porrunt otatior maxi­mil magni il endunt.</p>
    <p class="copy copy--two">Nem faccum vellabo. Ut lignatiosant ent qui dolorese veratiatquam quates et aut fuga. Pa­rum nonsers percti blatet quia cuscit, tes adit volest, offic te illamusciet dolorestiasi veliquu ntiorro voluptio quo minum et quisin conse­quam in net asperitem rae. Et hitios es ipsam rem alibus.</p>
  </section>

  <!-- Intro panel -->
  <section class="panel intro">
    <div class="brand">
      <span class="brand__dot"></span>
      <span class="brand__name">Hundeakademie<br>Auental</span>
    </div>
    <p class="kicker kicker--small">Hundeakademie Auental</p>
    <h2 class="headline">Vielfältige Trainingsangebote für Dich.</h2>
    <p class="lead">Du findest hier, modernes und effizientes Hundetraining. Die Trainingsmethoden basieren auf Basis positiver Verstärkung. So das Du mit Deinem Hund mit Spaß und Vertrauen, Dein Trainingsziel erreichst.</p>
    <p class="copy">Nem faccum vellabo. Ut lignatiosant ent qui dolorese veratiatquam quates et aut fuga. Pa­rum nonsers percti blatet quia cuscit, tes adit volest, offic te illamusciet dolorestiasi veliquu ntiorro voluptio quo minum et quisin conse­quam in net asperitem rae. Et hitios es ipsam rem alibus.</p>
    <div class="photo" role="img" aria-label="Foto eines liegenden, braun-weiß gefleckten Welpen"></div>
  </section>

  <!-- Offers panel -->
  <section class="panel panel--warm offers">
    <div class="offer" style="top:50px">
      <div class="offer__img" role="img" aria-label="Rundes Foto eines hellen Welpen" style="background:linear-gradient(160deg,#a8805a,#d9b27a,#7b5434)"></div>
      <span class="offer__label">Einzeltraining</span>
      <div class="offer__text">
        <p class="offer__title">1:1 Coaching</p>
        <p class="offer__desc">Optimal für Problemen oder exklusives Training</p>
        <p class="offer__target">Für Welpen, Jagdhunde oder erwachsene Hunde</p>
      </div>
    </div>
    <div class="offer" style="top:290px">
      <div class="offer__img" role="img" aria-label="Rundes Foto einer Hundegruppe beim Training" style="background:linear-gradient(160deg,#6f8a6a,#b59a78,#5a3b23)"></div>
      <span class="offer__label">Gruppentraining</span>
      <div class="offer__text">
        <p class="offer__title">Spaß in der Gruppe</p>
        <p class="offer__desc">Optimal für Alltagstraining und Beschäftigung</p>
        <p class="offer__target">Für Welpen, Jagdhunde oder erwachsene Hunde</p>
      </div>
    </div>
    <div class="offer" style="top:530px">
      <div class="offer__img" role="img" aria-label="Rundes Foto eines rotbraunen Hundes mit Halterin" style="background:linear-gradient(160deg,#4d5a4a,#b0652e,#7b5434)"></div>
      <span class="offer__label">Workshops</span>
      <div class="offer__text">
        <p class="offer__title">Kompaktes Training</p>
        <p class="offer__desc">Optimal für effektives Training in kurzer Zeit</p>
        <p class="offer__target">Für Hunde ab 10 Monaten</p>
      </div>
    </div>
  </section>

  <!-- Right panel -->
  <section class="panel story">
    <p class="kicker kicker--small">Fundiertes Training, Beratung mit Herz</p>
    <p class="lead lead--one">Du möchtest, dass Dein Hund verlässlig ist und Du ihm im Alltag vertrauen kannst?</p>
    <p class="lead lead--two">Spaß und ein Gefühl der Sicherheit sollen auch dabei sein? Ich lege Wert darauf, damit Du Deinen Hund besser verstehst.</p>
    <p class="lead lead--three">Du wirst zu einem Freund für Deinen Hund, der ihm wohlwollend und liebevoll den Weg in unserem Alltag zeigt.</p>
    <span class="badge"></span>
    <div class="photo" role="img" aria-label="Foto von Hunden an der Leine in einem Birkenwald"></div>
  </section>

</body>
</html>
```